New Zealand Marlborough Sauvignon Blanc wine packaging design

We need packaging design for our new wine brand, Dunmore Hale. The wine is a New Zealand Marlborough Sauvignon Blanc. We would like the packaging will portray elegance and style with an understated label. We are looking for a label that portrays the elegance of the French Riviera. The label should be round or pill shaped.
Updates

Industry/Entity Type

Wine

Font styles to use
Serif
Sans Serif

Requirements
Must have
• The words in order of importance: Dunmore Hale, Sauvignon Blanc, Marlborough, New Zealand. It should be fit to the bottle posted in the links
Nice to have
• a pill shape or circular shape
Should not have
• Illustrations of wine bottles, wine glasses, or grapes

```html
<!DOCTYPE html>
<html lang="en">
<head>
<meta charset="utf-8">
<title>Dunmore Hale — Marlborough Sauvignon Blanc Label</title>
<link rel="stylesheet" href="https://fonts.googleapis.com/css2?family=Crimson+Text:wght@400&family=Playball&display=swap">
<style>
  :root {
    --page: #ffffff;
    --label-paper: #ffffff;
    --label-edge: #c9c1bc;
    --ink: #5e4e4a;
    --sky: #dbe6f3;
    --blossom: #e9619f;
    --foliage: #a9bdb1;
    --copper: #b5542c;
  }
  html, body {
    margin: 0;
    padding: 0;
    width: 849px;
    height: 1200px;
    overflow: hidden;
    background: var(--page);
  }
  .canvas {
    position: relative;
    width: 849px;
    height: 1200px;
    display: flex;
    align-items: center;
    justify-content: center;
  }
  .wine-label {
    width: 600px;
    height: 795px;
    display: block;
  }
  .label-paper { fill: var(--label-paper); }
  .label-scallop {
    fill: none;
    stroke: var(--label-edge);
    stroke-width: 1.4;
    stroke-dasharray: 2 2.2;
  }
  .label-rule {
    fill: none;
    stroke: var(--label-edge);
    stroke-width: 0.8;
  }
  .label-outline {
    fill: none;
    stroke: #e4dfdc;
    stroke-width: 1;
  }
  .varietal-panel { fill: var(--sky); }
  .region, .country {
    font-family: "Crimson Text", Georgia, serif;
    font-size: 15px;
    letter-spacing: 2.6px;
    fill: var(--ink);
  }
  .brand-name {
    font-family: "Playball", cursive;
    font-size: 50px;
    fill: var(--copper);
  }
  .varietal {
    font-family: "Crimson Text", Georgia, serif;
    font-size: 24px;
    fill: var(--ink);
  }
</style>
</head>
<body>
<main class="canvas">
  <svg class="wine-label" viewBox="0 0 400 530" xmlns="http://www.w3.org/2000/svg" aria-label="Dunmore Hale Marlborough Sauvignon Blanc label">
    <defs>
      <linearGradient id="blossom-tones" x1="0" y1="0" x2="1" y2="1">
        <stop offset="0" stop-color="#e36aa2"/>
        <stop offset="0.55" stop-color="#d99abb"/>
        <stop offset="1" stop-color="#b7c8bd"/>
      </linearGradient>
      <path id="region-arc" d="M 90 112 A 140 140 0 0 1 310 112"/>
      <path id="country-arc" d="M 92 455 A 140 140 0 0 0 308 455"/>
    </defs>

    <!-- label body and edges -->
    <ellipse class="label-paper" cx="200" cy="265" rx="199" ry="264"/>
    <ellipse class="label-outline" cx="200" cy="265" rx="199" ry="264"/>
    <ellipse class="label-scallop" cx="200" cy="265" rx="191" ry="256"/>
    <ellipse class="label-rule" cx="200" cy="265" rx="186" ry="251"/>

    <!-- arched scene window -->
    <path class="scene-window" role="img" aria-label="Bougainvillea blossoms and leaves against a pale sky"
          fill="url(#blossom-tones)"
          d="M 48 262 L 48 252 A 151 151 0 0 1 350 252 L 350 250 Q 300 255 260 252 Q 220 248 180 258 Q 120 266 48 262 Z"/>

    <!-- lower varietal panel -->
    <path class="varietal-panel"
          d="M 53 355 Q 110 348 170 354 Q 230 360 345 352 Q 330 470 200 472 Q 72 470 53 355 Z"/>

    <text class="region"><textPath href="#region-arc" startOffset="50%" text-anchor="middle">MARLBOROUGH</textPath></text>

    <text class="brand-name" x="200" y="325" text-anchor="middle">Dunmore Hale</text>

    <text class="varietal" x="200" y="393" text-anchor="middle">Sauvignon Blanc</text>

    <text class="country"><textPath href="#country-arc" startOffset="50%" text-anchor="middle" dominant-baseline="hanging">NEW ZEALAND</textPath></text>
  </svg>
</main>
</body>
</html>
```